Vornix 1デザイン(2サイズ)
Kelpa 1デザイン(2サイズ)
TALLWIRE 1デザイン(2サイズ)

6つのバナーですが、デザインは3種類(各2サイズ)で、作成をお願いします。

3つの掲載先(Vornix、Kelpa、Tallwire)を検討しています。
3つの広告は、デザインを違うものでお願いします。

リンク先のランディングページをつながるデザインでお願いします。
https://kmt-qs.jp/opt-in/

参考のために、母体となるサイトのURLも記載します。
https://kmt-qs.jp/

素材は、購入してください。
こちらから、データ提供できるものはございません。
デザイナーと連絡が取れなくなってしまって、元データがありません。
グラフデータなどもランディングページ内にあるものを作成してください。

どうそ、よろしくお願いいたします。

定期的なhtmlメルマガなどの作成ができる方など、継続的にお願いできる方だとありがたいです。
細かなこだわりはないので、提案をくださるかた、スピーディーにたたき台を作成していただける方、自主的に進めてくれる方を探しております。
強調したいポイント(すべてを入れていただく必要はありません)
・売上アップ
・300万円の助成金
・離職を減らす
・塾の経営
・国に頼らない

というキーワードを出したいです。

あと、売上アップのグラフなど(ランディングページ内)。
• 添付ファイル参照
シンプル 複雑
単色 カラフル
暗い 明るい
日常 高級
遊び心 厳粛
未来的 伝統的
女性的 男性的
• 高解像度JPG (.jpg)
• イラストレーター形式 (.ai)
• フォトショップ形式 (.psd)
• PNG形式 (.png)
サイズは添付ファイルに記載しております。

```html
<!DOCTYPE html>
<html lang="ja">
<head>
<meta charset="UTF-8">
<title>放課後デイサービス向け VR教育教材</title>
<link href="https://fonts.googleapis.com/css2?family=Noto+Sans+JP:wght@500;700;900&display=swap" rel="stylesheet">
<style>
  :root{
    --frame:#fbe84a;
    --paper:#ffffff;
    --blue:#2f9fe0;
    --coral:#f46a6c;
    --green:#5cbf5a;
    --red:#e8402f;
    --arrow:#e84a3c;
    --ink:#333333;
    --axis:#1e9bd7;
    --gold:#ffd21f;
  }
  *{margin:0;padding:0;box-sizing:border-box;}
  html,body{width:675px;height:1200px;overflow:hidden;background:var(--paper);}
  body{font-family:"Noto Sans JP",sans-serif;color:var(--ink);}
  .banner{position:relative;width:675px;height:1200px;background:var(--frame);overflow:hidden;}
  .banner__inner{position:absolute;left:22px;top:22px;right:22px;bottom:22px;background:var(--paper);}
  .photo{position:absolute;left:22px;top:230px;width:418px;height:456px;
    background:linear-gradient(135deg,#c9c3bb 0%,#e8e2da 45%,#4e6a58 100%);}
  .shapes{position:absolute;left:0;top:0;width:675px;height:1200px;}
  .chart-text{font-family:"Noto Sans JP",sans-serif;}
  .label{position:absolute;text-align:center;font-weight:900;white-space:nowrap;}
  .label--target{left:30px;top:72px;width:240px;color:#fff;font-size:34px;line-height:57px;}
  .label--title{left:250px;top:169px;width:396px;color:#fff;font-size:54px;line-height:90px;}
  .label--result{left:18px;top:841px;width:200px;color:var(--ink);font-size:40px;line-height:52px;}
  .label--result .up{color:var(--red);}
  .label--result .down{color:var(--blue);}
</style>
</head>
<body>
<div class="banner">
  <div class="banner__inner"></div>
  <div class="photo" role="img" aria-label="VRゴーグルを着けて笑顔の生徒の写真"></div>

  <svg class="shapes" viewBox="0 0 675 1200" xmlns="http://www.w3.org/2000/svg">
    <defs>
      <linearGradient id="arrowFade" x1="0" y1="1" x2="0" y2="0">
        <stop offset="0" stop-color="var(--arrow)" stop-opacity="0.05"/>
        <stop offset="1" stop-color="var(--arrow)" stop-opacity="0.95"/>
      </linearGradient>
    </defs>

    <rect class="chart-panel" x="259" y="440" width="394" height="738" fill="#fff"/>

    <g class="bars">
      <rect x="270" y="972" width="113" height="153" fill="#fff" stroke="#ddd" stroke-width="2"/>
      <rect x="270" y="945" width="113" height="27" fill="var(--blue)"/>
      <rect x="517" y="837" width="113" height="288" fill="#fff" stroke="#ddd" stroke-width="2"/>
      <rect x="517" y="540" width="113" height="297" fill="var(--red)"/>
    </g>
    <g class="chart-text" font-weight="700" text-anchor="middle">
      <text x="326" y="964" font-size="16" fill="#fff">純利益</text>
      <text x="326" y="1060" font-size="19" fill="#333">費用</text>
      <text x="573" y="707" font-size="21" fill="#fff">純利益</text>
      <text x="573" y="1000" font-size="19" fill="#333">費用</text>
      <text x="326" y="1166" font-size="21" fill="#333">放デイのみ</text>
      <text x="573" y="1166" font-size="21" fill="var(--red)">事業導入後</text>
    </g>

    <path class="up-arrow" d="M320 880 L320 700 L285 700 L345 625 L405 700 L370 700 L370 880 Z" fill="url(#arrowFade)"/>
    <text x="428" y="792" text-anchor="middle" font-size="58" font-weight="900" fill="var(--red)" class="chart-text">UP!</text>

    <g class="callout-before">
      <rect x="271" y="884" width="111" height="48" rx="4" fill="#333"/>
      <path d="M318 932 L326 941 L334 932 Z" fill="#333"/>
      <g class="chart-text" fill="#fff" text-anchor="middle" font-weight="700">
        <text x="326" y="903" font-size="14">売上</text>
        <text x="326" y="925" font-size="20">3,500<tspan font-size="14">万円</tspan></text>
      </g>
    </g>
    <g class="callout-after">
      <rect x="472" y="479" width="180" height="61" fill="var(--gold)"/>
      <g class="chart-text" text-anchor="middle" font-weight="900" fill="var(--red)">
        <text x="562" y="501" font-size="17">売上</text>
        <text x="562" y="532" font-size="30">6,000<tspan font-size="20">万円</tspan></text>
      </g>
    </g>

    <polygon class="hex-target" points="150,14 290,72 290,190 150,250 10,190 10,72" fill="var(--blue)" stroke="#fff" stroke-width="6"/>
    <polygon class="hex-title" points="448,34 645,150 645,330 448,440 250,330 250,150" fill="var(--coral)" stroke="#fff" stroke-width="8"/>
    <polygon class="hex-result" points="118,776 232,840 232,1050 118,1114 16,1050 16,840" fill="#fff" stroke="var(--green)" stroke-width="10"/>

    <g class="axis chart-text" font-size="15" fill="#fff" font-weight="700" text-anchor="middle">
      <text x="224" y="540" fill="#666" font-size="15" font-weight="500">(万円)</text>
      <rect x="198" y="583" width="54" height="26" fill="var(--axis)"/><text x="225" y="601">6,000</text>
      <rect x="198" y="712" width="54" height="26" fill="var(--axis)"/><text x="225" y="730">5,000</text>
      <rect x="198" y="849" width="54" height="26" fill="var(--axis)"/><text x="225" y="867">4,000</text>
      <rect x="198" y="977" width="54" height="26" fill="var(--axis)"/><text x="225" y="995">3,000</text>
      <rect x="198" y="1123" width="54" height="26" fill="var(--axis)"/><text x="225" y="1141">2,000</text>
    </g>
  </svg>

  <div class="label label--target">放課後<br>デイサービス<br>向け</div>
  <div class="label label--title">VRを使った<br>教育教材</div>
  <div class="label label--result">売上<br><span class="up">アップ</span>で<br>離職率は<br><span class="down">ダウン</span></div>
</div>
</body>
</html>
```